Culture consulting company business card - first step

I created a new venture called The Summit Ledger. It's focused on improving the organizational culture of companies and I have a logo, tag line and other basic info but I need an overall design theme I'll carry through to letterhead, marketing literature, direct mail post cards, whitepapers, video intros and my web site. The business card design is a trial to develop the theme and more projects will hopefully follow for the winner! This business will grow fast and I need a great design theme to leverage.

Target Market(s)

Target Market is both for profit and non profit businesses. Special emphasis on consulting companies, foundations and venture capital firms

Industry/Entity Type

Marketing

Requirements
Must have
• The Summit Ledger Logo
Name (Dan Prewitt)
Phone (555-417-6290)
E-mail (Dan@The-Summit-Ledger.example)
Web Site (www.The-Summit-Ledger.example)
Tag line in some way: "Culture Change with Clarity and Speed"
- Clarity and Speed should be in red with speed potentially in italics. The other words in black.

Front and back of card design - front has info above
Back should have The Summit Ledger logo and a list of areas we focus on with the red check mark image next to each. The areas are: Performance Improvement, Organizational Excellence, Strategic Alignment, Team Effectiveness, Onboarding, Leadership Development & Coaching

Overall key colors are in the logo (red & black)

NEED DESIGN FORMAT in a PHOTOSHOP / PSD FILE. Photoshop template from printer is attached. Needs to follow the diminsions / guidelines.
Nice to have
• Potentially "road" picture if it fits with a great theme
Should not have
• Needs to be veryprofessional looking but it's fine to come across as very innovative, interesting or unique. Need clear design / fonts and color theme I can carry through to other print and web formats.

```html
<!DOCTYPE html>
<html lang="en">
<head>
<meta charset="utf-8">
<title>The Summit Ledger – Business Card</title>
<link href="https://fonts.googleapis.com/css2?family=Arimo:ital,wght@0,400;0,700;1,700&display=swap" rel="stylesheet">
<style>
  :root {
    --red: #e0202f;
    --black: #111111;
    --paper: #eeeeee;
    --white: #ffffff;
    --ink: #1a1a1a;
    --backdrop: #d9d9d9;
    --road-light: #c9c9c9;
    --road-dark: #6e6e6e;
  }
  * { box-sizing: border-box; margin: 0; padding: 0; }
  html, body {
    width: 1200px; height: 880px; overflow: hidden;
    background: var(--backdrop);
    font-family: "Arimo", Arial, sans-serif;
  }
  .card {
    position: absolute; left: 250px;
    width: 700px; height: 400px;
    overflow: hidden;
    box-shadow: 0 6px 18px rgba(0,0,0,.25);
  }
  .card-front { top: 30px; background: var(--paper); }
  .card-back { top: 450px; background: var(--black); }
  .card-shapes { position: absolute; inset: 0; }

  .brand-name {
    position: absolute;
    font-weight: 700; color: var(--red);
    text-transform: uppercase; letter-spacing: 1px;
    line-height: 1.05;
  }
  .brand-name::before {
    content: ""; display: inline-block;
    width: 14px; height: 14px; background: var(--red);
    margin-right: 10px; vertical-align: 2px;
  }
  .card-front .brand-name { left: 56px; top: 78px; font-size: 30px; }

  .contact {
    position: absolute; left: 420px; top: 112px;
    padding-left: 22px;
    border-left: 1px solid #b5b5b5;
    color: var(--ink); font-size: 14px; line-height: 1.45;
  }
  .contact-name { color: var(--red); font-weight: 700; font-size: 19px; margin-bottom: 4px; }
  .contact-label { color: var(--red); margin-right: 4px; }

  .tagline {
    position: absolute; left: 48px; top: 262px;
    color: var(--white); font-size: 20px;
    transform: rotate(9deg); transform-origin: left center;
  }
  .tagline .accent { color: var(--red); font-weight: 700; }
  .tagline .accent-speed { font-style: italic; }

  .card-back .brand-name { left: 28px; top: 196px; font-size: 22px; width: 230px; }

  .focus-list {
    position: absolute; left: 300px; top: 58px;
    list-style: none; color: var(--white);
    font-size: 17px; line-height: 1.6;
  }
  .focus-list li { display: flex; align-items: center; gap: 10px; }
  .tick { width: 16px; height: 14px; flex: none; }
  .website {
    position: absolute; left: 300px; top: 330px;
    color: var(--red); font-weight: 700; font-size: 18px;
  }
</style>
</head>
<body>

<section class="card card-front">
  <svg class="card-shapes" viewBox="0 0 700 400" aria-hidden="true">
    <path d="M0,196 C220,214 430,330 700,282 L700,300 C430,346 220,232 0,214 Z" fill="var(--red)"/>
    <path d="M0,222 C220,240 430,352 700,306 L700,400 L0,400 Z" fill="var(--black)"/>
  </svg>
  <div class="brand-name">The Summit Ledger</div>
  <div class="contact">
    <div class="contact-name">Dan Prewitt</div>
    <div><span class="contact-label">p:</span>555-417-6290</div>
    <div><span class="contact-label">e:</span>Dan@The-Summit-Ledger.example</div>
    <div><span class="contact-label">w:</span>www.The-Summit-Ledger.example</div>
  </div>
  <p class="tagline">Culture Change with <span class="accent">Clarity</span> and <span class="accent accent-speed">Speed</span></p>
</section>

<section class="card card-back">
  <svg class="card-shapes" viewBox="0 0 700 400">
    <defs>
      <linearGradient id="roadTone" x1="0" y1="0" x2="1" y2="1">
        <stop offset="0" stop-color="var(--road-dark)"/>
        <stop offset=".45" stop-color="var(--road-light)"/>
        <stop offset="1" stop-color="#9a9a9a"/>
      </linearGradient>
    </defs>
    <path role="img" aria-label="Black and white photograph of an open road curving into the distance"
          d="M0,0 L262,0 C230,140 270,280 218,400 L0,400 Z" fill="url(#roadTone)"/>
    <path d="M262,0 C230,140 270,280 218,400" fill="none" stroke="var(--red)" stroke-width="8"/>
  </svg>
  <div class="brand-name">The Summit Ledger</div>
  <ul class="focus-list">
    <li><svg class="tick" viewBox="0 0 16 14"><path d="M1,8 L6,13 L15,1" fill="none" stroke="var(--red)" stroke-width="3"/></svg>Performance Improvement</li>
    <li><svg class="tick" viewBox="0 0 16 14"><path d="M1,8 L6,13 L15,1" fill="none" stroke="var(--red)" stroke-width="3"/></svg>Organizational Excellence</li>
    <li><svg class="tick" viewBox="0 0 16 14"><path d="M1,8 L6,13 L15,1" fill="none" stroke="var(--red)" stroke-width="3"/></svg>Strategic Alignment</li>
    <li><svg class="tick" viewBox="0 0 16 14"><path d="M1,8 L6,13 L15,1" fill="none" stroke="var(--red)" stroke-width="3"/></svg>Team Effectiveness</li>
    <li><svg class="tick" viewBox="0 0 16 14"><path d="M1,8 L6,13 L15,1" fill="none" stroke="var(--red)" stroke-width="3"/></svg>Onboarding</li>
    <li><svg class="tick" viewBox="0 0 16 14"><path d="M1,8 L6,13 L15,1" fill="none" stroke="var(--red)" stroke-width="3"/></svg>Leadership Development</li>
    <li><svg class="tick" viewBox="0 0 16 14"><path d="M1,8 L6,13 L15,1" fill="none" stroke="var(--red)" stroke-width="3"/></svg>Coaching</li>
  </ul>
  <div class="website">www.The-Summit-Ledger.example</div>
</section>

</body>
</html>
```